Kelvora trustee touch - styling

We have a prototyped single page application. The content is in place what we need is restyling to

- make it more user friendly
- modern look and feel
- improve accessibility features
- use our brand guidelines (screen shots attached of the full website)

Prototype is available at http://plinthdesk.examplehost.net/

Target form factor:
Primary - tablet
Secondary - desktop

Target Market(s)

Business users - not financial professionals but people working for big companies who have some limited training in the concepts

Number of Pages Required

1 page

Requirements
Must have
• Touch user interface

```html
<!DOCTYPE html>
<html lang="en">
<head>
<meta charset="utf-8">
<title>Kelvora – Trustee Touch</title>
<link rel="stylesheet" href="https://fonts.googleapis.com/css2?family=Open+Sans:wght@400;600;700&display=swap">
<style>
:root{
  --brand-blue:#0b5fb1;
  --brand-blue-dark:#0d4a85;
  --tab-blue:#114f8d;
  --tab-divider:#2a66a3;
  --magenta:#a5155f;
  --ink-blue:#1b4e86;
  --stat-1:#0a3c70;
  --stat-2:#0d4781;
  --stat-3:#0e4f8f;
  --stat-4:#0d579f;
  --area-blue:#b4cfe8;
  --area-pink:#d9a1c2;
  --grid:#e6e6e6;
  --band:#f6f6f6;
  --track:#d9d9d9;
  --handle:#666;
  --text:#555;
  --white:#fff;
  --footer:#0f4a80;
}
*{box-sizing:border-box;margin:0;padding:0}
html,body{width:1200px;height:768px;overflow:hidden;background:var(--white)}
body{font-family:"Open Sans",Arial,sans-serif;position:relative;color:var(--text)}

.site-header{position:absolute;left:0;top:0;width:1200px;height:83px;background:linear-gradient(90deg,#0a5db0,#0c63b4)}
.brand{position:absolute;left:28px;top:20px;font-size:31px;font-weight:700;color:var(--white);letter-spacing:-0.5px}
.context-nav{position:absolute;left:566px;top:0;height:83px;display:flex}
.context-nav a{display:flex;align-items:center;justify-content:center;height:83px;color:var(--white);text-decoration:none;font-size:15px;background:var(--tab-blue);border-left:1px solid var(--tab-divider)}
.context-nav a.is-active{background:var(--magenta);border-left:none}

.chart-card{position:absolute;left:28px;top:104px;width:824px;height:402px;background:var(--white);border:1px solid #dcdcdc;box-shadow:0 1px 3px rgba(0,0,0,.12)}
.chart-card svg{position:absolute;left:-28px;top:-104px}

.stats{position:absolute;left:851px;top:104px;width:321px;height:401px}
.stat{height:100px;display:flex;flex-direction:column;align-items:center;justify-content:center;color:var(--white);border-bottom:1px solid rgba(255,255,255,.12)}
.stat:nth-child(1){background:var(--stat-1)}
.stat:nth-child(2){background:var(--stat-2)}
.stat:nth-child(3){background:var(--stat-3)}
.stat:nth-child(4){background:var(--stat-4);border-bottom:none}
.stat-value{font-size:22px;font-weight:600;line-height:30px;display:flex;align-items:center;gap:10px}
.stat-label{font-size:14px;line-height:20px}

.control{position:absolute;top:540px;width:399px}
.control-title{text-align:center;font-size:18px;font-weight:600;line-height:26px}
.control-title.invest{color:var(--ink-blue)}
.control-title.contrib{color:var(--magenta)}
.slider{position:relative;height:16px;margin-top:22px;background:var(--track)}
.slider-fill{position:absolute;left:0;top:0;height:16px}
.slider-handle{position:absolute;top:-8px;width:11px;height:29px;background:var(--handle)}
.slider-scale{display:flex;justify-content:space-between;font-size:14px;margin-top:13px}

.lock{position:absolute;left:918px;top:572px}

.site-footer{position:absolute;left:0;top:715px;width:1200px;height:53px;background:var(--footer);color:var(--white);font-size:14px}
.site-footer .copyright{position:absolute;left:0;right:0;top:18px;text-align:center}
.site-footer .version{position:absolute;right:26px;top:18px}
</style>
</head>
<body>
<header class="site-header">
  <div class="brand">Kelvora</div>
  <nav class="context-nav">
    <a class="is-active" href="#" style="width:120px">XYZ Limited</a>
    <a href="#" style="width:181px">XYZ Pension Scheme</a>
    <a href="#" style="width:177px">Technical Provisions</a>
    <a href="#" style="width:129px">October 2014</a>
  </nav>
</header>

<section class="chart-card" aria-label="Flight Plan chart">
  <svg width="880" height="520" viewBox="0 0 880 520" font-family="Open Sans, Arial, sans-serif">
    <g class="bands" fill="var(--band)">
      <rect x="130" y="100" width="658" height="42"/>
      <rect x="130" y="186" width="658" height="42"/>
      <rect x="130" y="270" width="658" height="42"/>
      <rect x="130" y="356" width="658" height="42"/>
    </g>
    <path d="M130 290 L224 300 L318 270 L412 205 L506 272 L600 180 L694 188 L788 192 L788 440 L130 440Z" fill="#efefef" opacity=".7"/>
    <g class="grid" stroke="var(--grid)" stroke-width="1">
      <line x1="224" y1="100" x2="224" y2="440"/><line x1="318" y1="100" x2="318" y2="440"/>
      <line x1="412" y1="100" x2="412" y2="440"/><line x1="506" y1="100" x2="506" y2="440"/>
      <line x1="600" y1="100" x2="600" y2="440"/><line x1="694" y1="100" x2="694" y2="440"/>
      <line x1="788" y1="100" x2="788" y2="440"/>
    </g>
    <path d="M130 366 L224 336 L318 337 L412 253 L506 293 L600 208 L694 209 L788 251 L788 440 L130 440Z" fill="var(--area-blue)"/>
    <path d="M130 376 L224 408 L318 383 L412 407 L506 324 L600 367 L694 240 L788 412 L788 440 L130 440Z" fill="var(--area-pink)"/>
    <line x1="130" y1="100" x2="130" y2="440" stroke="#cfcfcf"/>
    <line x1="130" y1="440" x2="788" y2="440" stroke="#cfcfcf"/>
    <polyline points="130,366 224,336 318,337 412,253 506,293 600,208 694,209 788,251" fill="none" stroke="var(--ink-blue)" stroke-width="4" stroke-linejoin="round"/>
    <polyline points="130,376 224,408 318,383 412,407 506,324 600,367 694,240 788,412" fill="none" stroke="var(--magenta)" stroke-width="4" stroke-linejoin="round"/>
    <g fill="var(--ink-blue)" stroke="#fff" stroke-width="2">
      <circle cx="224" cy="336" r="7"/><circle cx="318" cy="337" r="7"/><circle cx="412" cy="253" r="7"/>
      <circle cx="506" cy="293" r="7"/><circle cx="600" cy="208" r="7"/><circle cx="694" cy="209" r="7"/>
    </g>
    <g fill="var(--magenta)" stroke="#fff" stroke-width="2">
      <circle cx="224" cy="408" r="7"/><circle cx="318" cy="383" r="7"/><circle cx="412" cy="407" r="7"/>
      <circle cx="506" cy="324" r="7"/><circle cx="600" cy="367" r="7"/><circle cx="694" cy="240" r="7"/>
    </g>
    <text x="443" y="168" text-anchor="middle" font-size="18" font-weight="600" fill="var(--ink-blue)">Flight Plan</text>
    <g font-size="12" fill="#555" text-anchor="end">
      <text x="116" y="227">160%</text><text x="116" y="270">140%</text><text x="116" y="312">120%</text>
      <text x="116" y="354">100%</text><text x="116" y="396">80%</text><text x="116" y="438">60%</text>
    </g>
    <g font-size="11" font-weight="600" fill="#666" text-anchor="middle">
      <text x="219" y="465">23rd Feb 14</text><text x="315" y="465">24th Feb 14</text><text x="414" y="465">25th Feb 14</text>
      <text x="511" y="465">26th Feb 14</text><text x="605" y="465">27th Feb 14</text><text x="705" y="465">28th Feb 14</text>
      <text x="786" y="465">2014</text>
    </g>
  </svg>
</section>

<aside class="stats">
  <div class="stat"><div class="stat-value">91%</div><div class="stat-label">Funding Level</div></div>
  <div class="stat"><div class="stat-value">2,5%
    <svg width="14" height="16" viewBox="0 0 14 16" aria-hidden="true"><path d="M7 0 L14 8 H9.5 V16 H4.5 V8 H0Z" fill="#fff"/></svg></div>
    <div class="stat-label">Funding Level change</div></div>
  <div class="stat"><div class="stat-value">3%&nbsp;
    <svg width="14" height="16" viewBox="0 0 14 16" aria-hidden="true"><path d="M7 16 L14 8 H9.5 V0 H4.5 V8 H0Z" fill="#fff"/></svg></div>
    <div class="stat-label">Progress against fight plan</div></div>
  <div class="stat"><div class="stat-value">67%</div><div class="stat-label">10 yr project funding level</div></div>
</aside>

<section class="control" style="left:28px">
  <h2 class="control-title invest">Investment Strategy</h2>
  <div class="slider"><div class="slider-fill" style="width:231px;background:var(--ink-blue)"></div><div class="slider-handle" style="left:233px"></div><div style="position:absolute;left:244px;top:0;width:2px;height:16px;background:#fff"></div></div>
  <div class="slider-scale"><span>Matching</span><span style="margin-left:60px">50% / 50%</span><span>Growth</span></div>
</section>

<section class="control" style="left:459px">
  <h2 class="control-title contrib">Contributions</h2>
  <div class="slider"><div class="slider-fill" style="width:231px;background:var(--magenta)"></div><div class="slider-handle" style="left:233px"></div><div style="position:absolute;left:244px;top:0;width:2px;height:16px;background:#fff"></div></div>
  <div class="slider-scale"><span>£0m</span><span style="margin-left:80px">£16.6m</span><span>£30m</span></div>
</section>

<svg class="lock" width="30" height="38" viewBox="0 0 30 38" role="img" aria-label="Unlocked">
  <path d="M7 16 V10 a8 8 0 0 1 16 0 V12" fill="none" stroke="#555" stroke-width="5"/>
  <rect x="2" y="15" width="26" height="21" rx="2" fill="#555"/>
</svg>

<footer class="site-footer">
  <div class="copyright">© 2014 Kelvora All Rights Reserved.</div>
  <div class="version">M3</div>
</footer>
</body>
</html>
```